Constant Contact email marketing template

I need engaging customizable templates that can be used in multiple fundraising campaigns.

I included a school bus project that we used in a previous campaign. This campaign, however, is a $25 for $25 promotion. Consumers make a $25 contribution for the school or charity and receive back a $25 e-gift card to be used at area restaurants.

Important! This is a completely generic piece, capable of being used in schools, churches, or other civic organizations.

The 5 part example is NOT what I am looking for. I included it to suggest the concept. I am looking forward to viewing YOUR designs,

Target Market(s)

schools, leagues, nonprofit organizations

Font styles to use
Sans Serif

Colors

Designer to choose colors to be used in the design.

Requirements
Must have
• Must clearly present itself as a fundraising tool for schools, leagues and Nonprofit organizations.
• Must have 2 clickable buttons that allow member to click

```html
<!DOCTYPE html>
<html lang="en">
<head>
<meta charset="utf-8">
<title>Greatest Fundraising Event – $25 for $25</title>
<link href="https://fonts.googleapis.com/css2?family=Montserrat:wght@700;800;900&family=Roboto:ital,wght@0,400;0,500;0,700;1,400;1,500&display=swap" rel="stylesheet">
<style>
:root{
  --grey-bg:#f1f2f4;
  --cyan:#12c8e6;
  --cyan-dark:#0aa6c4;
  --teal-text:#0b5a66;
  --yellow:#f4e21a;
  --pink:#f4566e;
  --cream:#fdf1ec;
  --red:#e2230f;
  --red-price:#e8261a;
  --navy:#13303a;
  --body-text:#555555;
  --charcoal:#474747;
  --white:#ffffff;
  --footer-text:#444444;
}
*{box-sizing:border-box;margin:0;padding:0}
html,body{width:1200px;height:3436px;overflow:hidden;background:var(--white)}
body{font-family:'Roboto',Arial,sans-serif;position:relative}
.section{position:absolute;left:0;width:1200px}

.preheader{top:0;height:118px;background:var(--grey-bg);display:flex;align-items:center;justify-content:center;font-size:24px;color:#333}
.preheader a{color:#333;margin-left:8px;text-decoration:underline}

.hero{top:118px;height:860px;background:linear-gradient(135deg,#7a4a2e 0%,#a4542f 30%,#c77a3c 55%,#6b3b22 80%,#3e2416 100%)}
.hero-header{position:absolute;top:0;left:0;width:1200px;height:200px}
.hero-title{position:absolute;top:20px;width:100%;text-align:center;color:var(--white);font-family:'Roboto',sans-serif;font-weight:700;font-size:60px;letter-spacing:1px}
.hero-subtitle{position:absolute;top:100px;width:100%;text-align:center;color:var(--teal-text);font-family:'Montserrat',sans-serif;font-weight:700;font-size:30px;letter-spacing:7px}
.hero-headline{position:absolute;top:290px;width:100%;text-align:center;color:var(--yellow);font-family:'Montserrat',sans-serif;font-weight:900;font-size:78px;letter-spacing:2px}
.hero-tagline{position:absolute;top:385px;width:100%;text-align:center;color:var(--white);font-family:'Montserrat',sans-serif;font-weight:800;font-size:40px;letter-spacing:1px}
.gift-cards-art{position:absolute;left:220px;top:555px;width:790px;height:130px;background:linear-gradient(90deg,#e0566a,#f4c73a,#6fae4f,#2d9be0,#e23b3b,#2db8d8,#e05a3a);opacity:.85;border-radius:6px}
.deal-box{position:absolute;left:167px;top:680px;width:859px;height:156px;background:linear-gradient(90deg,#3fd8f2,#0fc4e4);border-radius:10px;color:var(--white)}
.deal-line{position:absolute;font-size:22px;color:#0d3340}
.deal-line b{font-size:32px;color:var(--white);font-weight:700}
.deal-line.l1{left:50px;top:18px}
.deal-line.l2{left:110px;top:58px}
.deal-line.l3{left:310px;top:100px}
.deal-line.l3 b{font-size:28px}
.deal-tab{position:absolute;left:0;bottom:0;width:200px;height:56px;background:var(--cyan-dark);border-radius:0 10px 0 10px;color:var(--white);font-size:24px;display:flex;align-items:center;justify-content:center;font-weight:500}
.web-tag{position:absolute;right:-10px;top:-14px;background:var(--red);color:var(--white);font-weight:700;font-style:italic;font-size:20px;padding:10px 22px;border-radius:6px}

.why{top:978px;height:543px;background:var(--pink);color:var(--white);text-align:center}
.why-title{margin-top:42px;display:inline-block;font-size:50px;font-weight:700;padding-bottom:10px;border-bottom:5px solid var(--white)}
.why-list{list-style:none;margin-top:44px;font-style:italic;font-weight:500;font-size:30px;line-height:46px}

.org-photo{top:1521px;height:399px;background:linear-gradient(160deg,#6b6a68 0%,#9a948c 35%,#4d4f55 65%,#2a2c33 100%)}
.org-caption{position:absolute;left:362px;top:332px;color:var(--white);font-size:25px;font-weight:500}

.offer{top:1920px;height:780px;background:var(--cream);text-align:center}
.offer-price{margin-top:30px;font-weight:700;line-height:1}
.offer-price .amount{color:var(--red-price);font-size:124px}
.offer-price .for{color:var(--navy);font-size:76px;margin-left:18px}
.offer-rule{width:460px;height:5px;background:var(--pink);margin:28px auto 0}
.offer-copy{margin:60px auto 0;width:900px;color:var(--body-text);font-size:28px;line-height:41px}
.offer-copy p{margin-bottom:28px}
.offer-copy .hl{color:var(--pink)}
.offer-actions{position:absolute;top:594px;left:196px;display:flex;gap:24px}
.btn{width:391px;height:106px;background:var(--red);color:var(--white);border-radius:10px;display:flex;flex-direction:column;align-items:center;justify-content:center;text-decoration:none;font-weight:500}
.btn-primary{font-size:32px}
.btn-secondary{font-size:32px;line-height:38px}
.btn-secondary small{font-size:27px}

.fineprint{top:2700px;height:334px;background:var(--charcoal);color:var(--white);text-align:center;font-size:21px;line-height:29px;padding-top:34px}
.fineprint p{margin-bottom:22px}

.social{top:3034px;height:166px;background:var(--grey-bg);display:flex;align-items:center;justify-content:center;gap:44px}
.social-item{display:flex;align-items:center;gap:10px;font-size:22px;color:#333;font-weight:500;text-decoration:none}
.social-dot{width:22px;height:22px;border-radius:50%;background:#777}

.footer{top:3200px;height:236px;text-align:center;color:var(--footer-text);font-size:21px;line-height:30px;padding-top:60px}
.footer a{color:var(--footer-text);text-decoration:underline}
.footer p{margin-bottom:14px}
</style>
</head>
<body>

<div class="section preheader">Don't see this email properly? <a href="#">View in web browser</a></div>

<header class="section hero">
  <div role="img" aria-label="Photo of a pizza with tomatoes, garlic and chili peppers on a wooden table" style="position:absolute;inset:0"></div>
  <svg class="hero-header" viewBox="0 0 1200 200" width="1200" height="200" aria-hidden="true">
    <polygon points="0,0 1200,0 1200,150 600,200 0,150" fill="#0aa6c4"/>
    <polygon points="0,0 1200,0 1200,130 600,180 0,130" fill="#12c8e6"/>
  </svg>
  <h1 class="hero-title">Greatest Fundraising Event</h1>
  <div class="hero-subtitle">COMPANY/CHARITY NAME GOES HERE</div>
  <h2 class="hero-headline">ENJOY GREAT FOOD</h2>
  <div class="hero-tagline">WHILE SUPPORTING A GREAT CAUSE</div>
  <div class="gift-cards-art" role="img" aria-label="Fan of colourful restaurant gift cards valued $15 to $50"></div>
  <div class="deal-box">
    <div class="web-tag">www.dinegive.org</div>
    <div class="deal-line l1">Redeem for more than <b>5000,000 DEALS</b> nationwide</div>
    <div class="deal-line l2"><b>THOUSANDS OF NEW RESTAURANTS</b> added every month</div>
    <div class="deal-line l3"><b>PLUS</b> our cards <b>NEVER, EVER EXPIRE</b></div>
    <div class="deal-tab">e-Gift Cards</div>
  </div>
</header>

<section class="section why">
  <h2 class="why-title">WHY E-GIFT CARDS?</h2>
  <ul class="why-list">
    <li>- Local, independent neighbougood restaurants -</li>
    <li>- More than 62,000+ restaurants providers nationwide-</li>
    <li>- More than 3.5 million Verified Dinner Reviews -</li>
    <li>- More than 500,000 deals available every day -</li>
    <li>Thousands of new restaurants added every month -</li>
    <li>Always available, NEVER expire -</li>
  </ul>
</section>

<section class="section org-photo" role="img" aria-label="Photo of the church, organisation or charity">
  <div class="org-caption">Image of Church/Organisation/Charity</div>
</section>

<section class="section offer">
  <div class="offer-price"><span class="amount">$25</span><span class="for">for $25</span></div>
  <div class="offer-rule"></div>
  <div class="offer-copy">
    <p>We're raising revenue for your favorite <span class="hl">church/charity/school</span> and we're happy to send you our best offer yet.</p>
    <p>Your contribution is a real <span class="hl">WIN-WIN</span> in this fundraiser.</p>
    <p>You simply donate $25 and we you $25 back in <span class="hl">e-Gift Cards</span> for your restaurants in your area.</p>
  </div>
  <div class="offer-actions">
    <a class="btn btn-primary" href="#">DONATE NOW</a>
    <a class="btn btn-secondary" href="#">DONATE on behalf<small>of a loved one or friend</small></a>
  </div>
</section>

<section class="section fineprint">
  <p>This is a fundraising project conducted by Hearth 12 Marketing Group, Inc.<br>fo rthe benefit of your comapny name.</p>
  <p>This is a limited time offer. Additional e-Gift Cards can be bought as gifts.<br>Proceeds on this project are for your comapny name.<br>E-Gift Cards can be used for up to 50% of tab in each visit.</p>
  <p>The remainder stays on the card for following purchases. Present e-Gift Card to the server at<br>time of ordering. Other restrictions may appaly.</p>
</section>

<nav class="section social">
  <a class="social-item" href="#"><span class="social-dot"></span>Friendly</a>
  <a class="social-item" href="#"><span class="social-dot"></span>Chirper</a>
  <a class="social-item" href="#"><span class="social-dot"></span>Circles</a>
  <a class="social-item" href="#"><span class="social-dot"></span>Snapshot</a>
  <a class="social-item" href="#"><span class="social-dot"></span>Pinboard</a>
</nav>

<footer class="section footer">
  <p>H12 Group, Inc &nbsp;|&nbsp; 4821 Marlow Ave, Suite 210, Box 52, Springfield, TX 78000</p>
  <p><a href="#">Unsubscribe</a> (recipients email)</p>
  <p><a href="#">Update Profile</a> &nbsp;|&nbsp; <a href="#">About our service provider</a></p>
  <p>Sent by support@dinegive.org in collaboration with company name</p>
</footer>

</body>
</html>
```